" Nome da empresa: Recanto Vivale CLINICA DE NUTRIÇAO SOMOS NUTRICIONISTAS E DESEJAMOS PROPORCIONAR AOS NOSSOS PACIENTES UM TRATAMENTO INDIVIDUALIZADO. FAREMOS ATENDIMENTOS NUTRICIONAIS A FIM DE LEVAR QUALIDADE DE VIDA E PREVENÇAO de doenças, focando na educaçao nutricional "

```html
<!DOCTYPE html>
<html lang="pt-BR">
<head>
<meta charset="UTF-8">
<title>Recanto Vivale – Cartão de visita</title>
<link href="https://fonts.googleapis.com/css2?family=Ubuntu:wght@400;500&display=swap" rel="stylesheet">
<style>
  :root {
    --page-bg: #efebe5;
    --card-white: #ffffff;
    --card-green: #1e5a4f;
    --brand-teal: #2e6b63;
    --tagline: #5f8a7e;
    --ink-light: #ffffff;
    --ink-soft: #d7e6e1;
  }
  * { margin: 0; padding: 0; box-sizing: border-box; }
  html, body {
    width: 1200px;
    height: 1200px;
    overflow: hidden;
    background: var(--page-bg);
    font-family: "Ubuntu", sans-serif;
  }
  .card {
    position: absolute;
    left: 192px;
    top: 485px;
    width: 907px;
    height: 211px;
    display: flex;
    box-shadow: 0 6px 16px rgba(0,0,0,0.18);
  }
  .card-front {
    width: 324px;
    height: 100%;
    background: var(--card-white);
    position: relative;
  }
  .brand-name {
    position: absolute;
    left: 62px;
    top: 114px;
    font-size: 31px;
    font-weight: 500;
    color: var(--brand-teal);
    white-space: nowrap;
  }
  .brand-tagline {
    position: absolute;
    left: 64px;
    top: 152px;
    font-size: 9px;
    color: var(--tagline);
    white-space: nowrap;
  }
  .card-back {
    flex: 1;
    height: 100%;
    background: var(--card-green);
    position: relative;
    color: var(--ink-light);
  }
  .person-name {
    position: absolute;
    left: 20px;
    top: 56px;
    font-size: 17px;
    font-weight: 400;
  }
  .person-role {
    position: absolute;
    left: 58px;
    top: 77px;
    font-size: 9px;
    color: var(--ink-soft);
  }
  .contact-list {
    position: absolute;
    left: 22px;
    top: 104px;
    list-style: none;
    font-size: 9.5px;
    line-height: 18px;
    color: var(--ink-soft);
  }
  .contact-list .address { line-height: 14px; margin-top: 2px; }
</style>
</head>
<body>
  <section class="card">
    <div class="card-front">
      <div class="brand-name">Recanto Vivale</div>
      <div class="brand-tagline">Saúde Clínica e Educação Nutricional</div>
    </div>
    <div class="card-back">
      <div class="person-name">Nome Sobrenome</div>
      <div class="person-role">Função</div>
      <ul class="contact-list">
        <li>Tel: 0000-0000</li>
        <li>Cel: 0000-0000</li>
        <li>Email: contato@recantovivale.com.br</li>
        <li class="address">Endereço Rua das Flores,00 Bairro<br>Jardins, Cidade das Flores</li>
      </ul>
    </div>
  </section>
</body>
</html>
```